Website design with eCommerce for revolutionary new product in the manufacturing industry.

We need a website designed for a precision manufacturing company based in the suburbs of Minneapolis, Minnesota called Velkor Manufacturing. We have a revolutionary new product, the TRIM LATCH, to introduce and sell through an eCommerce storefront. The website would include company information, product information, and the storefront. Green is a color that represents Velkor Manufacturing. The final design should communicate that we exclusively offer premium products at a premium price. The design should also let the customer know they are the focus of our work.

Target Market(s)

Machinists and machine shops

Industry/Entity Type

Manufacturing and machine shops

Coding

Coded - Design and coding required

Font styles to use
Sans Serif

Colors
59FF00
82FF00
B8FF75
E3FFCB
F4FFEA

Requirements
Must have
• eCommerce storefront, Made in USA references
Nice to have
• Home page, TRIM LATCH Product page, About Us, Capabilities, Contact, etc.
Should not have
• Should not be too much text and reading.

```html
<!DOCTYPE html>
<html lang="en">
<head>
<meta charset="utf-8">
<title>Velkor Manufacturing</title>
<link href="https://fonts.googleapis.com/css2?family=Montserrat:wght@400;500;600;700;800&display=swap" rel="stylesheet">
<style>
:root{
  --green:#3ea21f;
  --green-bright:#6fd13a;
  --ink:#1b1b1b;
  --text:#4a4a4a;
  --muted:#777;
  --line:#e3e3e3;
  --white:#fff;
  --dark:#1c1c1c;
}
*{box-sizing:border-box;margin:0;padding:0}
html,body{width:1200px;height:3659px;overflow:hidden}
body{font-family:'Montserrat',sans-serif;color:var(--ink);background:var(--white);position:relative}
.abs{position:absolute}
a{color:inherit;text-decoration:none}

/* header */
.site-header{position:absolute;top:0;left:0;width:1200px;height:71px;background:var(--white)}
.brand{position:absolute;font-weight:800;font-size:25px;letter-spacing:1px;color:var(--ink)}
.site-header .brand{left:158px;top:22px}
.main-nav{position:absolute;left:390px;top:29px;display:flex;gap:28px;font-size:11px;font-weight:500;letter-spacing:.3px}
.main-nav .active{color:var(--ink)}
.main-nav .active::before{content:"➜ ";color:var(--green)}
.phone{position:absolute;left:918px;top:25px;font-size:15px;font-weight:700;display:flex;align-items:center;gap:8px}

/* hero */
.hero{position:absolute;top:71px;left:0;width:1200px;height:491px;background:radial-gradient(ellipse at 70% 45%,#4a4a46 0%,#2b2b29 45%,#151514 100%)}
.hero-product{position:absolute;left:780px;top:60px;width:250px;height:340px;background:linear-gradient(160deg,#3fb02a,#1e6d16);border-radius:8px;opacity:.85}
.hero-faint{position:absolute;left:156px;top:85px;font-size:80px;font-weight:800;color:rgba(255,255,255,.08);letter-spacing:2px}
.hero h1{position:absolute;left:157px;top:185px;font-size:46px;line-height:48px;font-weight:800;color:var(--white)}
.hero h1 span{color:var(--green-bright)}
.hero p{position:absolute;left:158px;top:292px;width:360px;font-size:13px;line-height:19px;font-weight:600;color:var(--white)}
.btn-outline{position:absolute;border:1.5px solid var(--white);color:var(--white);font-size:12px;font-weight:600;border-radius:3px;text-align:center}
.hero .btn-outline{left:158px;top:350px;width:131px;height:37px;line-height:34px}

/* why */
.down-arrow{position:absolute;left:589px;top:594px}
.eyebrow{position:absolute;left:0;width:1200px;text-align:center;font-size:12px;color:var(--green);font-weight:500}
.section-title{position:absolute;left:0;width:1200px;text-align:center;font-size:21px;line-height:24px;font-weight:500;color:var(--ink)}
.feature{position:absolute;top:810px;display:flex;align-items:center;gap:16px}
.feature .icon-box{width:64px;height:56px;border:1px solid var(--line);border-radius:4px;display:flex;align-items:center;justify-content:center}
.feature p{font-size:13px;line-height:16px;color:var(--muted)}

/* what we do */
.what{position:absolute;top:939px;left:0;width:1200px;height:414px;background:linear-gradient(120deg,#5a4a2a 0%,#1f3f7a 35%,#1a3b78 100%)}
.what-panel{position:absolute;left:663px;top:42px;width:365px;height:330px;border-radius:14px;background:linear-gradient(140deg,#a88a48,#4c3e22 60%,#1d3466)}
.what h2{position:absolute;left:158px;top:60px;font-size:21px;font-weight:500;color:var(--white)}
.what h2 span{color:var(--green-bright)}
.what h3{position:absolute;left:156px;top:103px;width:420px;font-size:16px;line-height:20px;font-weight:600;color:var(--white)}
.what p{position:absolute;left:156px;width:400px;font-size:11px;line-height:15.5px;color:#e8e8e8}
.what .btn-outline{left:158px;top:296px;width:131px;height:37px;line-height:34px}

/* gallery */
.tile{position:absolute;top:1519px;height:239px;width:232px;background:linear-gradient(150deg,#bdbdbd,#6c6c6c)}
.slider-btn{position:absolute;top:1803px;width:28px;height:26px;display:flex;align-items:center;justify-content:center}

/* how better */
.better{position:absolute;top:1899px;left:0;width:1200px;height:390px;background:linear-gradient(180deg,#f3f3f3,#e9e9e9);overflow:hidden}
.better-product{position:absolute;left:150px;top:20px;width:380px;height:340px;border-radius:12px;background:linear-gradient(150deg,#47b530,#1c6a14)}
.better h2{position:absolute;left:596px;top:54px;font-size:21px;font-weight:500}
.better ul{position:absolute;left:596px;top:110px;list-style:none;width:420px}
.better li{position:relative;padding-left:28px;font-size:11px;line-height:17px;color:var(--text);margin-bottom:18px}
.better li svg{position:absolute;left:0;top:2px}
.btn-dark{position:absolute;left:598px;top:285px;width:130px;height:36px;background:#111;color:var(--white);font-size:12px;font-weight:600;line-height:36px;text-align:center;border-radius:3px}

/* capabilities */
.cap{position:absolute;width:240px}
.cap h4{font-size:15px;font-weight:600;margin-top:10px}
.cap h4::after{content:" —";color:var(--green)}
.cap p{font-size:11px;line-height:15.5px;color:var(--text);margin-top:6px;height:48px}
.cap .arrow{margin-top:10px}
.divider-v{position:absolute;width:1px;background:var(--line)}
.btn-green{position:absolute;background:var(--green);color:var(--white);font-weight:600;text-align:center;border-radius:3px}

/* contact */
.contact{position:absolute;top:3022px;left:0;width:1200px;height:460px;background:radial-gradient(ellipse at 60% 50%,#3c3c3c,#1a1a1a)}
.contact h2{position:absolute;left:156px;top:80px;font-size:21px;font-weight:500;color:var(--white)}
.field{position:absolute;left:158px;width:325px;height:36px;border:1px solid #8c8c8c;border-radius:3px;color:#bbb;font-size:11px;padding:11px 14px}
.contact-photo{position:absolute;left:625px;top:62px;width:419px;height:352px;border-radius:10px;background:linear-gradient(140deg,#2e2e2e,#1e1e1e);border:1px solid #3a3a3a}
.contact-photo .part{position:absolute;background:linear-gradient(160deg,#44b22c,#1f6e15);border-radius:6px}

/* footer */
.site-footer .brand{left:160px;top:3535px}
.foot-nav{position:absolute;left:437px;top:3545px;display:flex;gap:22px;font-size:11px;font-weight:500}
.foot-nav span.sep{color:var(--ink)}
.foot-line{position:absolute;left:0;top:3590px;width:1200px;height:1px;background:var(--line)}
.copyright{position:absolute;left:158px;top:3617px;font-size:10px;color:var(--text)}
.social{position:absolute;top:3612px;width:22px;height:22px;border-radius:50%;background:#d8d8d8}
</style>
</head>
<body>

<header class="site-header">
  <div class="brand">TRIM LATCH</div>
  <nav class="main-nav">
    <a class="active">HOME</a><a>CAPABILITIES</a><a>ABOUT US</a><a>GALLERY</a><a>WISDOM</a><a>CONTACT US</a>
  </nav>
  <div class="phone">
    <svg width="20" height="20" viewBox="0 0 24 24" fill="none" stroke="#111" stroke-width="2"><path d="M5 3h4l2 5-3 2a11 11 0 0 0 6 6l2-3 5 2v4a2 2 0 0 1-2 2A18 18 0 0 1 3 5a2 2 0 0 1 2-2z"/></svg>
    612 555 0148
  </div>
</header>

<section class="hero" role="img" aria-label="Green anodised latch product resting in dark machining chips">
  <div class="hero-faint">TRIM LATCH</div>
  <div class="hero-product"></div>
  <h1>WELCOME TO <span>VELKOR</span><br>MANUFACTURING</h1>
  <p>We are a machine shop with complete end to end manufacturing capabilities.</p>
  <a class="btn-outline">SHOP NOW</a>
</section>

<svg class="down-arrow" width="22" height="34" viewBox="0 0 22 34" fill="none" stroke="#333" stroke-width="1.5"><path d="M11 1v31M2 23l9 9 9-9"/></svg>
<div class="eyebrow" style="top:669px">Why Velkor Manufacturing?</div>
<h2 class="section-title" style="top:696px">BECAUSE THERE IS A BETTER WAY, AND WE WILL FIND IT,<br>EVEN IF IT'S THE HARD WAY.&nbsp; WE BELIEVE IN WORKING<br>HARDER AND SMARTER TO ACHIEVE SUCCESS.</h2>

<div class="feature" style="left:158px">
  <div class="icon-box"><svg width="30" height="26" viewBox="0 0 30 26" fill="none" stroke="#333" stroke-width="1.3"><path d="M2 24h26M6 24V16M11 24V11M16 24V14M21 24V7"/></svg></div>
  <p>Our success is measured<br>in your success</p>
</div>
<div class="feature" style="left:473px">
  <div class="icon-box"><svg width="30" height="30" viewBox="0 0 30 30" fill="none" stroke="#333" stroke-width="1.3"><circle cx="14" cy="16" r="11"/><circle cx="14" cy="16" r="6"/><circle cx="14" cy="16" r="1.5"/><path d="M14 16 26 4" stroke="#3ea21f"/></svg></div>
  <p>Focused on our your needs<br>and making excellent parts</p>
</div>
<div class="feature" style="left:802px">
  <div class="icon-box"><svg width="32" height="28" viewBox="0 0 32 28" fill="none" stroke="#333" stroke-width="1.3"><path d="M2 26h28M3 22l8-7 5 4 9-11"/><circle cx="26" cy="5" r="3"/></svg></div>
  <p>Exceeding your<br>expectations</p>
</div>

<section class="what" role="img" aria-label="Machined brass parts on a blue background">
  <div class="what-panel"></div>
  <h2>WHAT WE <span>DO</span> <svg width="48" height="16" viewBox="0 0 48 16" fill="none" stroke="#6fd13a" stroke-width="1.5"><path d="M0 5h40M0 11h40M36 1l10 7-10 7"/></svg></h2>
  <h3>We are a machine shop with complete end to end manufacturing capabilities.</h3>
  <p style="top:148px">We can take an idea or need, and bring it to a complete physical product.&nbsp; We can design and build your prototype, and we can mass produce it too.</p>
  <p style="top:209px">We love working directly with customers to manufacture their products, and help make it better where appropriate.&nbsp; We can work with as little as a verbal description, up to following fully defined customer specifications.</p>
  <a class="btn-outline">LEARN MORE</a>
</section>

<div class="eyebrow" style="top:1413px">Gallery</div>
<h2 class="section-title" style="top:1439px">HERE ARE SOME OF THE PROJECTS WE'VE<br>CREATED OVER THE YEARS.</h2>
<div class="tile" style="left:0;width:104px;background:linear-gradient(150deg,#b48d45,#2a4c86)" role="img" aria-label="Brass fixture blocks"></div>
<div class="tile" style="left:118px;background:linear-gradient(150deg,#d6d2c8,#7f7a70)" role="img" aria-label="Rows of machined aluminium rings"></div>
<div class="tile" style="left:362px;background:radial-gradient(circle at 50% 45%,#c8c8c8,#3a3a3a 70%)" role="img" aria-label="Machined triangular hub part"></div>
<div class="tile" style="left:606px;background:linear-gradient(150deg,#a6a49e,#4a4844)" role="img" aria-label="Grid of machined parts"></div>
<div class="tile" style="left:851px;background:radial-gradient(circle,#d8d8d8 0,#9a9a9a 60%,#777 62%,#8a8a8a)" role="img" aria-label="Perforated round metal disc"></div>
<div class="tile" style="left:1095px;width:105px;background:linear-gradient(150deg,#9a9a9a,#3a3a3a)" role="img" aria-label="Machined metal pins"></div>
<div class="slider-btn" style="left:568px;background:#cfcfcf"><svg width="8" height="12" fill="none" stroke="#333" stroke-width="1.5"><path d="M7 1 2 6l5 5"/></svg></div>
<div class="slider-btn" style="left:603px;background:var(--green-bright)"><svg width="8" height="12" fill="none" stroke="#111" stroke-width="1.5"><path d="M1 1l5 5-5 5"/></svg></div>

<section class="better">
  <svg class="abs" style="left:0;top:0" width="150" height="150"><path d="M0 0h110l40 60-150 90z" fill="#3ea21f"/></svg>
  <svg class="abs" style="left:1075px;top:230px" width="125" height="160"><path d="M125 0v160H50L0 100z" fill="#3ea21f"/></svg>
  <div class="better-product" role="img" aria-label="Green latch product with steel pin"></div>
  <h2>HOW WE MAKE IT BETTER <svg width="48" height="16" viewBox="0 0 48 16" fill="none" stroke="#6fd13a" stroke-width="1.5"><path d="M0 5h40M0 11h40M36 1l10 7-10 7"/></svg></h2>
  <ul>
    <li><svg width="15" height="15" viewBox="0 0 16 16" fill="none" stroke="#333" stroke-width="1.3"><circle cx="8" cy="8" r="6.5"/><path d="M5 8l2 2 5-5"/></svg>With 100 years of combined knowledge and experience to draw upon, we find solutions.</li>
    <li><svg width="15" height="15" viewBox="0 0 16 16" fill="none" stroke="#333" stroke-width="1.3"><circle cx="8" cy="8" r="6.5"/><path d="M5 8l2 2 5-5"/></svg>Our vast experience across multiple industries gives us insight that is invaluable in creativity and foresight.</li>
    <li><svg width="15" height="15" viewBox="0 0 16 16" fill="none" stroke="#333" stroke-width="1.3"><circle cx="8" cy="8" r="6.5"/><path d="M5 8l2 2 5-5"/></svg>This real life experience brings a broader understanding of what works, and more importantly, what doesn't work, ultimately allowing us to make more informed decisions.</li>
  </ul>
  <a class="btn-dark">LEARN MORE</a>
</section>

<div class="eyebrow" style="top:2352px">What can we do?</div>
<h2 class="section-title" style="top:2376px">WHILE THIS LIST COVERS MUCH OF OUR CAPABILITIES, IT<br>IS BY NO MEANS EXHAUSTIVE. YOU CAN ALWAYS<br>CONTACT US WITH SPECIFIC REQUESTS.</h2>

<div class="divider-v" style="left:427px;top:2500px;height:350px"></div>
<div class="divider-v" style="left:760px;top:2500px;height:350px"></div>
<div class="abs" style="left:148px;top:2675px;width:896px;height:1px;background:var(--line)"></div>

<div class="cap" style="left:158px;top:2494px">
  <svg width="48" height="44" viewBox="0 0 48 44" fill="none" stroke="#222" stroke-width="1.4"><rect x="2" y="2" width="44" height="32" rx="2"/><path d="M14 42h20M24 34v8M14 10l10-5 10 5v12l-10 5-10-5z"/></svg>
  <h4>CAD Design</h4><p>Do you have something that needs to be created, but no method of capturing the design?</p>
  <svg class="arrow" width="20" height="12" fill="none" stroke="#222" stroke-width="1.5"><path d="M0 6h18M13 1l5 5-5 5"/></svg>
</div>
<div class="cap" style="left:488px;top:2494px">
  <svg width="54" height="46" viewBox="0 0 54 46" fill="none" stroke="#222" stroke-width="1.4"><rect x="2" y="2" width="50" height="42" rx="3"/><path d="M2 12h50M22 22l-6 6 6 6M32 22l6 6-6 6M29 20l-4 16"/></svg>
  <h4>CAM Programming</h4><p>Do you need programs for your machines? Perhaps we can help. We use the latest 3D CAM</p>
  <svg class="arrow" width="20" height="12" fill="none" stroke="#222" stroke-width="1.5"><path d="M0 6h18M13 1l5 5-5 5"/></svg>
</div>
<div class="cap" style="left:819px;top:2494px">
  <svg width="46" height="46" viewBox="0 0 46 46" fill="none" stroke="#222" stroke-width="1.4"><path d="M23 2l10 5v10l-10 5-10-5V7zM4 24h38v12H4zM14 36v8h18v-8"/></svg>
  <h4>FFF 3D Printing</h4><p>Do you need a quick sample? Using Fused Filament Fabrication we can 3D print prototypes for</p>
  <svg class="arrow" width="20" height="12" fill="none" stroke="#222" stroke-width="1.5"><path d="M0 6h18M13 1l5 5-5 5"/></svg>
</div>
<div class="cap" style="left:158px;top:2698px">
  <svg width="50" height="46" viewBox="0 0 50 46" fill="none" stroke="#222" stroke-width="1.4"><rect x="2" y="12" width="44" height="30" rx="2"/><path d="M10 22h24M10 30h18"/><circle cx="24" cy="6" r="4" stroke="#3ea21f"/></svg>
  <h4>Prototypes</h4><p>Do you need a custom part, or test sample?<br>We can make custom, one-off parts such as racing components.</p>
  <svg class="arrow" width="20" height="12" fill="none" stroke="#222" stroke-width="1.5"><path d="M0 6h18M13 1l5 5-5 5"/></svg>
</div>
<div class="cap" style="left:488px;top:2698px">
  <svg width="46" height="46" viewBox="0 0 46 46" fill="none" stroke="#222" stroke-width="1.4"><path d="M4 4h38M10 4v8h26V4M18 12v10l5 6 5-6V12M6 38h34v6H6zM12 32h22"/></svg>
  <h4>Vertical CNC Machining</h4><p>with simultaneous 4th axis rotary<br>If you need parts processed through a vertical machining center, let us know.</p>
  <svg class="arrow" width="20" height="12" fill="none" stroke="#222" stroke-width="1.5"><path d="M0 6h18M13 1l5 5-5 5"/></svg>
</div>
<div class="cap" style="left:819px;top:2698px">
  <svg width="40" height="46" viewBox="0 0 40 46" fill="none" stroke="#222" stroke-width="1.4"><path d="M6 4h28M10 4v8h20V4M14 12l6 12 6-12M8 30l12 14 12-14z"/></svg>
  <h4>CNC Turning</h4><p>Collet or chuck work<br>If you need parts processed through a CNC lathe, let us know.</p>
  <svg class="arrow" width="20" height="12" fill="none" stroke="#222" stroke-width="1.5"><path d="M0 6h18M13 1l5 5-5 5"/></svg>
</div>

<a class="btn-green" style="left:504px;top:2916px;width:193px;height:37px;line-height:37px;font-size:12px">VIEW ALL CAPABILITIES</a>

<section class="contact">
  <h2>GET IN TOUCH WITH US</h2>
  <div class="field" style="top:116px">Name :</div>
  <div class="field" style="top:160px">Email :</div>
  <div class="field" style="top:204px">Phone :</div>
  <div class="field" style="top:248px;height:106px">Message :</div>
  <a class="btn-green" style="left:158px;top:360px;width:110px;height:34px;line-height:34px;font-size:12px">SUBMIT</a>
  <div class="contact-photo" role="img" aria-label="Two green latch products packed in a foam case with hex keys">
    <div class="part" style="left:45px;top:50px;width:120px;height:150px"></div>
    <div class="part" style="left:180px;top:25px;width:150px;height:270px"></div>
  </div>
</section>

<footer class="site-footer">
  <div class="brand">TRIM LATCH</div>
  <nav class="foot-nav">
    <a>HOME</a><span class="sep">|</span><a>CAPABILITIES</a><span class="sep">|</span><a>ABOUT US</a><span class="sep">|</span><a>GALLERY</a><span class="sep">|</span><a>WISDOM</a><span class="sep">|</span><a>CONTACT US</a>
  </nav>
  <div class="foot-line"></div>
  <div class="copyright">© Copyright 2022 Velkor Manufacturing | All rights reserved.</div>
  <div class="social" style="left:927px;background:var(--green)"></div>
  <div class="social" style="left:957px"></div>
  <div class="social" style="left:987px"></div>
  <div class="social" style="left:1017px"></div>
</footer>

</body>
</html>
```